Antigen Preservation Center

The company will provide a contract research services to stabilize various viruses, viral vectors, and vaccines. It may offer some licensing opportunities for stabilizing technologies. Main area of applications are pharmaceutical, therapeutic, and vaccination field. The company aspires to develop room temperature vaccines for global distribution beyond the current cold chain.
Updates

Target Market(s)

pharmaceutical, therapeutic and vaccination fields

Coding

Number of Pages Required

4 page

Requirements
Must have
• Incorporate a APC logo, attached at the bottom, on the Web page

```html
<!DOCTYPE html>
<html lang="en">
<head>
<meta charset="utf-8">
<title>Antigen Preservation Center</title>
<link href="https://fonts.googleapis.com/css2?family=Open+Sans:ital,wght@0,400;0,600;0,700;1,400&family=Poppins:wght@400;500;600&display=swap" rel="stylesheet">
<style>
:root{
  --green:#5fa38a;
  --gold:#cf9e3d;
  --grey:#8a8a8a;
  --ink:#1d1d1d;
  --text:#555;
  --light:#f4f4f4;
  --footer:#2f2f2f;
  --footer-bottom:#272727;
  --orange:#f0a46b;
  --link:#2b7fa8;
}
*{margin:0;padding:0;box-sizing:border-box}
html,body{width:1200px;height:3711px;overflow:hidden}
body{position:relative;font-family:"Open Sans",Arial,sans-serif;color:var(--text);background:#fff}
.abs{position:absolute}
.topbar{left:0;top:0;width:1200px;height:45px;background:var(--green);color:#fff;font-size:13px}
.topbar .info{left:99px;top:14px;display:flex;gap:28px}
.topbar .follow{left:767px;top:14px;display:flex;align-items:center;gap:14px}
.topbar .dot{width:10px;height:10px;border-radius:50%;background:#fff;display:inline-block}
.topbar .cta{left:943px;top:0;width:158px;height:45px;background:#6c6c6c;color:#fff;font-weight:700;font-size:12px;display:flex;align-items:center;justify-content:center}
.nav{left:0;top:45px;width:1200px;height:79px;background:#fff}
.brand{left:99px;top:18px;display:flex;align-items:center;gap:12px}
.brand .mark{width:40px;height:40px;border-radius:50%;background:var(--green)}
.brand .name{font-size:14px;font-weight:600;color:var(--green);line-height:1.25;letter-spacing:1.5px;text-transform:uppercase;width:200px}
.menu{top:32px;font-size:12px;font-weight:600;color:#222;text-transform:uppercase}
.hero{left:0;top:124px;width:1200px;height:613px;background:radial-gradient(ellipse at 25% 30%,#2e5d7a 0%,#0f2838 45%,#0a1a20 70%),#0a1a20}
.hero::after{content:"";position:absolute;inset:0;background:radial-gradient(circle at 88% 70%,rgba(110,140,70,.55),transparent 40%),radial-gradient(circle at 5% 90%,rgba(80,120,150,.35),transparent 35%)}
.hero-frame{left:190px;top:242px;width:822px;height:136px;border:3px solid #fff;border-top:none;z-index:2}
.hero-frame-top{top:242px;height:3px;background:#fff;z-index:2}
.hero-kicker{left:0;top:164px;width:1200px;text-align:center;color:#fff;font-size:15px;z-index:3}
.hero-title{left:0;top:211px;width:1200px;text-align:center;color:#fff;font-size:39px;line-height:48px;font-weight:600;z-index:3}
.hero-sub{left:0;top:266px;width:1200px;text-align:center;color:#fff;font-size:19px;font-weight:700;z-index:3}
.hero-btn{left:521px;top:358px;width:156px;height:44px;border:2px solid #fff;background:#13293a;color:#fff;font-size:12px;font-weight:700;display:flex;align-items:center;justify-content:center;z-index:3}
.badge{left:566px;top:700px;width:68px;height:68px;border-radius:50%;background:#fff;border:3px solid #eee;display:flex;align-items:center;justify-content:center;z-index:4}
.badge i{width:36px;height:36px;border-radius:50%;background:var(--green);display:block}
.kicker{width:1200px;left:0;text-align:center;font-size:14px;color:#555}
.heading{width:1200px;left:0;text-align:center;font-size:32px;font-weight:700;color:var(--ink)}
.rule{left:570px;width:60px;height:1px;background:#c9d9d2}
.band{left:0;top:1202px;width:1200px;height:505px;background:var(--green)}
.offer{top:950px;width:334px;height:426px;background:#fff;box-shadow:0 6px 16px rgba(0,0,0,.12);z-index:2}
.offer .photo{height:252px}
.offer h3{margin:24px 0 0 40px;font-size:19px;font-weight:700;color:var(--ink)}
.offer p{margin:16px 40px 0 40px;font-size:13px;line-height:1.65;color:#555}
.offer a{display:block;margin:8px 0 0 40px;font-size:11px;font-weight:700;color:var(--link)}
.about-1{left:0;top:1458px;width:1200px;text-align:center;color:#fff;font-size:30px}
.about-2{left:0;top:1494px;width:1200px;text-align:center;color:#fff;font-size:30px}
.about-2 b{font-weight:700}
.about-p{left:225px;top:1556px;width:750px;text-align:center;color:#e8f2ee;font-size:13px;line-height:1.75}
.app{top:1895px;height:158px;color:#fff;text-align:center}
.app svg{margin-top:24px}
.app h4{font-family:"Poppins",sans-serif;font-size:27px;font-weight:500;letter-spacing:1px;margin-top:4px}
.app small{display:block;font-size:12px;font-weight:700;margin-top:2px}
.grey-sec{left:0;top:2157px;width:1200px;height:559px;background:var(--light)}
.sec-kicker{font-size:14px;color:#555}
.sec-title{font-size:31px;font-weight:700;color:var(--ink)}
.article{left:94px;width:480px;display:flex;gap:28px}
.article .thumb{width:126px;height:89px;flex:none}
.article .date{font-size:12px;color:#6ab3d0;font-style:italic}
.article p{font-size:13px;line-height:1.7;color:#444;margin-top:20px}
.review{left:611px;top:2318px;width:487px;height:290px;background:#fff;box-shadow:0 4px 14px rgba(0,0,0,.1);padding:40px 44px}
.review q{display:block;font-style:italic;font-size:13.5px;line-height:1.8;color:#444;quotes:none}
.review .who{margin-top:24px;font-size:14px;font-weight:600;color:#222}
.review .loc{font-size:12px;color:#777}
.arrow{width:36px;height:36px;border-radius:50%;display:flex;align-items:center;justify-content:center;font-size:13px}
.map{left:0;top:2716px;width:1200px;height:441px;background:linear-gradient(135deg,#f1f1f1,#e3e3e3)}
.contact-box{left:99px;top:2791px;width:341px;height:284px;background:var(--gold);color:#fff;padding:34px 46px;box-shadow:0 6px 16px rgba(0,0,0,.18)}
.contact-box h5{font-size:21px;font-weight:600;margin-bottom:24px}
.contact-box li{list-style:none;display:flex;gap:18px;font-size:14px;line-height:1.55;margin-bottom:20px}
.strip{left:0;top:3157px;width:1200px;height:20px;background:var(--green)}
.footer{left:0;top:3177px;width:1200px;height:435px;background:var(--footer)}
.foot-title{font-size:13px;font-weight:700;letter-spacing:1.5px;color:#fff}
.txt{font-size:11.5px;line-height:1.65;color:#cfcfcf}
.tweet{display:flex;gap:14px;margin-top:22px}
.tweet i{flex:none;width:10px;height:10px;background:#777;border-radius:50%;margin-top:4px}
.links{font-size:11px;color:#cfcfcf;line-height:3.1}
.insta{width:69px;height:69px;background:#6a6a6a}
.sub-input{left:87px;top:3462px;width:240px;height:38px;border-radius:19px;background:#262626;font-size:11px;color:#777;padding:12px 18px}
.sub-btn{left:286px;top:3464px;width:34px;height:34px;border-radius:50%;background:var(--gold);display:flex;align-items:center;justify-content:center}
.bottom{left:0;top:3612px;width:1200px;height:99px;background:var(--footer-bottom)}
.soc{top:3660px;width:12px;height:12px;border-radius:50%;background:#bbb}
.copy{right:99px;top:3640px;font-size:11px;color:#888}
</style>
</head>
<body>

<header>
  <div class="abs topbar">
    <div class="abs info"><span>Phone: (555) 014-2290</span><span>support@apc-labs.org</span></div>
    <div class="abs follow"><span>Follow Us:</span><i class="dot"></i><i class="dot"></i><i class="dot"></i></div>
    <div class="abs cta">CONTAC US NOW</div>
  </div>
  <nav class="abs nav">
    <div class="abs brand"><span class="mark"></span><span class="name">Antigen Preservation Center</span></div>
    <span class="abs menu" style="left:443px">Home</span>
    <span class="abs menu" style="left:544px">About Us</span>
    <span class="abs menu" style="left:636px">Our Services</span>
    <span class="abs menu" style="left:760px">News &amp; Events</span>
    <span class="abs menu" style="left:892px">Partners</span>
    <span class="abs menu" style="left:990px">Contact</span>
    <svg class="abs" style="left:1082px;top:31px" width="16" height="16" viewBox="0 0 16 16"><circle cx="6.5" cy="6.5" r="5" fill="none" stroke="#222" stroke-width="2"/><line x1="10" y1="10" x2="15" y2="15" stroke="#222" stroke-width="2.2"/></svg>
  </nav>
</header>

<section class="abs hero" role="img" aria-label="Microscopic view of virus particles in deep blue and green">
  <div class="abs hero-frame"></div>
  <div class="abs hero-frame-top" style="left:190px;width:160px"></div>
  <div class="abs hero-frame-top" style="left:852px;width:160px"></div>
  <p class="abs hero-kicker">Goodness for since on because sniffed murky blinked</p>
  <h1 class="abs hero-title">Ask us How we can help</h1>
  <p class="abs hero-sub">We have the facilities and expert knowledge to meet your research needs.</p>
  <div class="abs hero-btn">LEARN MORE</div>
</section>
<div class="abs badge"><i></i></div>

<section>
  <p class="abs kicker" style="top:811px">For Better Welness &amp; Hope</p>
  <div class="abs rule" style="top:839px"></div>
  <h2 class="abs heading" style="top:852px">What We Offers</h2>
</section>

<div class="abs band"></div>
<article class="abs offer" style="left:101px">
  <div class="photo" role="img" aria-label="Blue virus particles" style="background:radial-gradient(circle at 40% 50%,#4fb3e6,#0f5a9c 70%)"></div>
  <h3>Stabilize various viruses</h3>
  <p>However judicious and ethic squarely labrad some preparatoy armdil aliqua enim ad minim veniam quis.</p>
  <a>READMORE</a>
</article>
<article class="abs offer" style="left:435px">
  <div class="photo" role="img" aria-label="Scientist working at a laboratory microscope" style="background:linear-gradient(135deg,#e9f1f5,#bcd2dd)"></div>
  <h3>Viral Vectors</h3>
  <p>However judicious and ethic squarely labrad some preparatoy armdil aliqua enim ad minim veniam quis.</p>
  <a>READMORE</a>
</article>
<article class="abs offer" style="left:769px">
  <div class="photo" role="img" aria-label="Syringe and vaccine vial" style="background:linear-gradient(135deg,#f4f6f7,#cfd8dc)"></div>
  <h3>Vaccines</h3>
  <p>However judicious and ethic squarely labrad some preparatoy armdil aliqua enim ad minim veniam quis.</p>
  <a>READMORE</a>
</article>

<section>
  <p class="abs about-1">About antigen preservation center</p>
  <p class="abs about-2"><b>Special Care</b> &amp; <b>Attention</b> they need</p>
  <p class="abs about-p">About psyco this however woodpecker from hey slackly contagiously and much under then bat iguanodon about divisive hello ducked goodness wow far one circa mischievous one excepting far bore speechlessly much ipsum dolor sit amet, consectetur adipisicing elit sed do eiusmod tempor incididunt labore et dolore.</p>
</section>

<section>
  <p class="abs kicker" style="top:1771px">Sample Dummy text</p>
  <h2 class="abs heading" style="top:1812px">Our Applications</h2>
  <div class="abs app" style="left:99px;width:312px;background:var(--gold)">
    <svg width="56" height="48" viewBox="0 0 56 48" fill="none" stroke="#fff" stroke-width="2.4"><rect x="10" y="14" width="36" height="30" rx="2"/><rect x="16" y="4" width="24" height="10"/><line x1="28" y1="22" x2="28" y2="36"/><line x1="21" y1="29" x2="35" y2="29"/></svg>
    <h4>Pharmaceutical</h4><small>readmore</small>
  </div>
  <div class="abs app" style="left:440px;width:315px;background:var(--green)">
    <svg width="56" height="48" viewBox="0 0 56 48" fill="none" stroke="#fff" stroke-width="2.4"><path d="M22 4h12M24 4v14L12 42h32L32 18V4"/><line x1="16" y1="32" x2="40" y2="32"/></svg>
    <h4>Therapeutic</h4><small>readmore</small>
  </div>
  <div class="abs app" style="left:787px;width:314px;background:var(--grey)">
    <svg width="56" height="48" viewBox="0 0 56 48" fill="none" stroke="#fff" stroke-width="2.4"><path d="M38 6l12 12M44 12l-8 8M34 12l10 10L20 46 10 36z M10 36l-6 6"/></svg>
    <h4>Vaccination</h4><small>readmore</small>
  </div>
</section>

<section class="abs grey-sec"></section>
<section>
  <p class="abs sec-kicker" style="left:94px;top:2190px">For Better Welness &amp; Hope</p>
  <h2 class="abs sec-title" style="left:94px;top:2234px">Recent Articles</h2>
  <div class="abs article" style="top:2318px">
    <div class="thumb" role="img" aria-label="Blue virus particles" style="background:radial-gradient(circle,#3f9fd8,#0b2f55)"></div>
    <div><span class="date">Posted: Sep 29, 2018</span><p>One wow wherever a that past reined bitterly racco became canny hypn tically you because ...</p></div>
  </div>
  <div class="abs article" style="top:2481px">
    <div class="thumb" role="img" aria-label="Red virus particle" style="background:radial-gradient(circle,#e46a7c,#5b8fc0)"></div>
    <div><span class="date">Posted: Sep 29, 2018</span><p>One wow wherever a that past reined bitterly racco became canny hypn tically you because ...</p></div>
  </div>
  <p class="abs sec-kicker" style="left:611px;top:2190px">For Better Welness &amp; Hope</p>
  <h2 class="abs sec-title" style="left:611px;top:2234px">Client Reviews</h2>
  <div class="abs review">
    <q>Medical prissy so smiling a before cantans kerously much notwit ahstan dingt hungry towards dear as darn more cavalier hatche pending rid boo yet more across caterpillar unwound terier crud misread less this globefish positively drank.</q>
    <p class="who">Elena Marsh</p>
    <p class="loc">Newyork, USA</p>
    <div class="abs arrow" style="left:362px;top:225px;border:1px solid #ddd;color:#999">&lsaquo;</div>
    <div class="abs arrow" style="left:406px;top:225px;background:var(--orange);color:#fff">&rsaquo;</div>
  </div>
</section>

<section>
  <div class="abs map" role="img" aria-label="Grey street map of the city centre"></div>
  <div class="abs contact-box">
    <h5>Contact Info</h5>
    <ul>
      <li><svg width="16" height="16" viewBox="0 0 16 16" fill="none" stroke="#fff" stroke-width="1.5"><circle cx="8" cy="8" r="7"/><path d="M1 8h14M8 1c3 3 3 11 0 14M8 1c-3 3-3 11 0 14"/></svg><span>1420 Larkin Row, Fairhaven<br>Oregon - 97402</span></li>
      <li><svg width="16" height="16" viewBox="0 0 16 16"><path d="M1 6l7-4 7 4v8H1z" fill="#fff"/><path d="M1 6l7 5 7-5" fill="none" stroke="#cf9e3d" stroke-width="1.4"/></svg><span>help@apc-labs.org</span></li>
      <li><svg width="16" height="16" viewBox="0 0 16 16"><path d="M3 1l3 3-2 2c1 2 3 4 5 5l2-2 3 3-2 3C7 14 2 9 1 3z" fill="#fff"/></svg><span>1-555-304-7781</span></li>
    </ul>
  </div>
  <div class="abs strip"></div>
</section>

<footer>
  <div class="abs footer"></div>
  <div class="abs" style="left:94px;top:3228px;width:48px;height:48px;border-radius:50%;background:#555"></div>
  <p class="abs txt" style="left:87px;top:3296px;width:230px">Vestibulum ante ipsum primis in faucs orci luctus et ultrices posuere Vestibulum ante ipsum primisVestibulum ante ipsum primis in faucs orci luctus et ultrices posuere</p>
  <h6 class="abs foot-title" style="left:87px;top:3422px">SUBSCRIBE US</h6>
  <div class="abs sub-input">Email subscribe</div>
  <div class="abs sub-btn"><svg width="14" height="14" viewBox="0 0 14 14"><path d="M1 7l12-6-5 12-2-4z" fill="#fff"/></svg></div>

  <div class="abs" style="left:351px;top:3244px;width:220px">
    <h6 class="foot-title">RECENT TWEETS</h6>
    <div class="tweet"><i></i><p class="txt">aVestibulum ante ipsum primis in faucs orci luctus et ultrices posuere Vestibulum ante ipsum</p></div>
    <div class="tweet"><i></i><p class="txt">aVestibulum ante ipsum primis in faucs orci luctus et ultrices posuere Vestibulum ante ipsum</p></div>
    <div class="tweet"><i></i><p class="txt">aVestibulum ante ipsum primis in faucs orci luctus et ultrices posuere Vestibulum ante ipsum</p></div>
  </div>

  <div class="abs" style="left:611px;top:3244px;width:220px">
    <h6 class="foot-title">QUICK LINK</h6>
    <div style="display:flex;gap:70px;margin-top:12px">
      <div class="links">Home<br>offerings<br>products<br>services<br>contact<br>about</div>
      <div class="links">About Us<br>Promotions<br>Contact Us</div>
    </div>
  </div>

  <div class="abs" style="left:876px;top:3244px;width:225px">
    <h6 class="foot-title">INSTAGRAM</h6>
    <div style="display:grid;grid-template-columns:repeat(3,69px);gap:12px 9px;margin-top:28px">
      <div class="insta"></div><div class="insta"></div><div class="insta"></div>
      <div class="insta"></div><div class="insta"></div><div class="insta"></div>
    </div>
  </div>

  <div class="abs bottom"></div>
  <i class="abs soc" style="left:87px"></i>
  <i class="abs soc" style="left:122px;background:var(--gold)"></i>
  <i class="abs soc" style="left:161px"></i>
  <i class="abs soc" style="left:199px"></i>
  <p class="abs copy">Copyright © 2018 www.apc-labs.org</p>
</footer>

</body>
</html>
```